I need a business card design for a new company that will be doing consulting work around issues of cultural competency, and diversity and inclusion. I would like the design to be crisp and clear with bold but conservative colors and incorporate shades of blue

Target Market(s)

Small businesses, schools, non-profits

Industry/Entity Type

Consulting

Font styles to use
Serif
Sans Serif

Colors
0c5ba6
6b449b
3276b5
0292cd

Requirements
Must have
• A Morrow Venture (name of company)
• Lemlem Tavish
• CEO
• lemlem@amorrowventure.com
• (215)483-2756

```html
<!DOCTYPE html>
<html lang="en">
<head>
<meta charset="utf-8">
<title>A Morrow Venture — Business Card</title>
<link rel="stylesheet" href="https://fonts.googleapis.com/css2?family=Domine:wght@700&family=Lato:wght@400;700&display=swap">
<style>
  :root {
    --page-bg: #e6e8eb;
    --card-top: #1a6bb8;
    --card-bottom: #0c5ba6;
    --ink: #ffffff;
    --ink-soft: rgba(255, 255, 255, 0.86);
    --accent-faint: rgba(255, 255, 255, 0.22);
    --accent-line: rgba(255, 255, 255, 0.28);
    --icon: rgba(255, 255, 255, 0.35);
  }
  html, body {
    margin: 0;
    width: 1200px;
    height: 900px;
    overflow: hidden;
    background: var(--page-bg);
  }
  .canvas {
    position: relative;
    width: 1200px;
    height: 900px;
    display: flex;
    align-items: center;
    justify-content: center;
  }
  .card {
    position: relative;
    width: 1000px;
    height: 572px;
    background: linear-gradient(160deg, var(--card-top) 0%, var(--card-bottom) 100%);
    box-shadow: 0 18px 40px rgba(0, 0, 0, 0.18);
    overflow: hidden;
    color: var(--ink);
    font-family: "Lato", sans-serif;
  }
  .decor {
    position: absolute;
    inset: 0;
  }
  .brand {
    position: absolute;
    left: 72px;
    top: 112px;
    display: flex;
    align-items: center;
    gap: 22px;
  }
  .brand-mark {
    width: 78px;
    height: 78px;
    border-radius: 50%;
    background: var(--accent-faint);
  }
  .brand-name {
    font-family: "Domine", serif;
    font-weight: 700;
    font-size: 36px;
    line-height: 1;
    letter-spacing: 0.5px;
  }
  .brand-tagline {
    margin-top: 6px;
    font-size: 22px;
    letter-spacing: 0.8px;
    color: var(--ink-soft);
  }
  .person {
    position: absolute;
    right: 140px;
    top: 132px;
    text-align: right;
  }
  .person-name {
    font-size: 34px;
    font-weight: 400;
    letter-spacing: 1.5px;
    text-transform: uppercase;
  }
  .person-role {
    margin-top: 2px;
    font-size: 20px;
    letter-spacing: 1px;
    color: var(--ink-soft);
  }
  .contact {
    position: absolute;
    left: 120px;
    top: 300px;
    list-style: none;
    margin: 0;
    padding: 0;
  }
  .contact-item {
    display: flex;
    align-items: center;
    gap: 20px;
    height: 46px;
    font-size: 24px;
    letter-spacing: 0.6px;
  }
  .contact-icon {
    width: 24px;
    height: 24px;
    flex: none;
  }
</style>
</head>
<body>
<main class="canvas">
  <section class="card" aria-label="Business card of Lemlem Tavish, A Morrow Venture">
    <svg class="decor" width="1000" height="572" viewBox="0 0 1000 572" aria-hidden="true">
      <!-- corner triangles top right -->
      <polygon points="900,30 940,70 870,70" fill="rgba(255,255,255,0.22)"/>
      <polygon points="930,80 965,80 965,120" fill="rgba(255,255,255,0.18)"/>
      <polygon points="955,125 985,165 955,165" fill="rgba(255,255,255,0.15)"/>
      <!-- small triangle left of brand -->
      <polygon points="0,135 40,150 0,170" fill="rgba(255,255,255,0.16)"/>
      <!-- divider line with node -->
      <line x1="0" y1="500" x2="580" y2="500" stroke="rgba(255,255,255,0.28)" stroke-width="4"/>
      <circle cx="612" cy="500" r="24" fill="rgba(255,255,255,0.22)"/>
      <line x1="644" y1="500" x2="1000" y2="500" stroke="rgba(255,255,255,0.28)" stroke-width="4"/>
    </svg>

    <div class="brand">
      <div class="brand-mark"></div>
      <div>
        <div class="brand-name">A Morrow Venture</div>
        <div class="brand-tagline">Consulting Company</div>
      </div>
    </div>

    <div class="person">
      <div class="person-name">Lemlem Tavish</div>
      <div class="person-role">CEO</div>
    </div>

    <ul class="contact">
      <li class="contact-item">
        <svg class="contact-icon" viewBox="0 0 24 24" aria-hidden="true">
          <path d="M6.6 10.8a15.1 15.1 0 0 0 6.6 6.6l2.2-2.2a1 1 0 0 1 1-.25 11.4 11.4 0 0 0 3.6.57 1 1 0 0 1 1 1V20a1 1 0 0 1-1 1A17 17 0 0 1 3 4a1 1 0 0 1 1-1h3.5a1 1 0 0 1 1 1c0 1.25.2 2.45.57 3.57a1 1 0 0 1-.25 1z" fill="rgba(255,255,255,0.35)"/>
        </svg>
        <span>(215)483 - 2756</span>
      </li>
      <li class="contact-item">
        <svg class="contact-icon" viewBox="0 0 24 24" aria-hidden="true">
          <path d="M2 11 22 3 15 21 11 13z" fill="rgba(255,255,255,0.35)"/>
        </svg>
        <span>lemlem@amorrowventure.com</span>
      </li>
      <li class="contact-item">
        <svg class="contact-icon" viewBox="0 0 24 24" aria-hidden="true">
          <g fill="none" stroke="rgba(255,255,255,0.35)" stroke-width="1.6">
            <circle cx="12" cy="12" r="9.5"/>
            <ellipse cx="12" cy="12" rx="4" ry="9.5"/>
            <line x1="2.5" y1="12" x2="21.5" y2="12"/>
            <line x1="4" y1="7" x2="20" y2="7"/>
            <line x1="4" y1="17" x2="20" y2="17"/>
          </g>
        </svg>
        <span>www.amorrowventure.com</span>
      </li>
    </ul>
  </section>
</main>
</body>
</html>
```